Narvelo - Human Capital Consultancy Business Cards

We need a business card design for a new professional services consulting company which is focused on People, Performance, Profit. Hence the company name "Narvelo Pty Ltd". We intend to work with organisations predominantly on achieving optimal business performance through it's people. Developing both individual and organisational capability through effective learning and talent management strategies. We also plan to offer leadership programs which look at how people can utilise wellness, mindfulness and resilience to enable them and their teams to perform more effectively. We are looking for something quite dynamic, even sporty looking rather than a staid'professional services' look. Please see logo attached.

Leadership

```html
<!DOCTYPE html>
<html lang="en">
<head>
<meta charset="utf-8">
<title>Narvelo Pty Ltd – Business Cards</title>
<link rel="stylesheet" href="https://fonts.googleapis.com/css2?family=Open+Sans:wght@400;600;700&display=swap">
<style>
  :root {
    --page-bg: #e9e7e4;
    --card-silver-light: #f4f4f4;
    --card-silver-dark: #c9c9c9;
    --ink-dark: #2b2b2b;
    --ink-logo: #4a4a4a;
    --accent-orange: #e2531f;
    --blue-deep: #1a2d8f;
    --blue-mid: #2648c4;
    --blue-light: #3b7ee0;
    --white: #ffffff;
    --rule: #3a3a3a;
  }
  * { box-sizing: border-box; margin: 0; padding: 0; }
  html, body { width: 1200px; height: 900px; overflow: hidden; }
  body {
    background: var(--page-bg);
    font-family: "Open Sans", sans-serif;
    position: relative;
  }
  .card {
    position: absolute;
    left: 315px;
    width: 570px;
    height: 335px;
    border-radius: 30px;
    overflow: hidden;
    box-shadow: 0 6px 18px rgba(0,0,0,0.18);
  }
  /* Front: silver contact card */
  .card--front {
    top: 70px;
    background: linear-gradient(135deg, var(--card-silver-light) 0%, #e2e2e2 55%, var(--card-silver-dark) 100%);
    color: var(--ink-dark);
  }
  .front__brand {
    position: absolute;
    left: 40px;
    top: 105px;
    width: 230px;
    text-align: center;
  }
  .brand-mark {
    display: inline-flex;
    align-items: center;
    gap: 10px;
  }
  .brand-mark__dot {
    width: 18px; height: 18px; border-radius: 50%;
    background: var(--accent-orange);
  }
  .brand-mark__name {
    font-size: 42px;
    font-weight: 700;
    color: var(--ink-logo);
    letter-spacing: 0.5px;
  }
  .tagline {
    margin-top: 18px;
    font-size: 15px;
    font-weight: 600;
    color: var(--ink-logo);
    white-space: nowrap;
  }
  .front__rule {
    position: absolute;
    left: 300px;
    top: 42px;
    width: 2px;
    height: 240px;
    background: var(--rule);
  }
  .front__details {
    position: absolute;
    left: 325px;
    top: 40px;
    font-size: 13.5px;
    line-height: 1.4;
  }
  .contact-name { font-size: 17px; font-weight: 700; }
  .contact-company { font-weight: 700; margin-top: 14px; }
  .contact-phones { margin-top: 16px; }
  .contact-phones b { font-weight: 700; }

  /* Back: blue brand card */
  .card--back {
    top: 475px;
    background: linear-gradient(120deg, var(--blue-deep) 0%, var(--blue-mid) 55%, var(--blue-light) 80%, var(--blue-mid) 100%);
    color: var(--white);
    text-align: center;
  }
  .back__brand {
    position: absolute;
    left: 0; right: 0;
    top: 100px;
  }
  .back__brand .brand-mark__name { color: var(--white); font-size: 50px; }
  .back__brand .brand-mark__dot { background: var(--white); width: 20px; height: 20px; }
  .back__brand .tagline { color: var(--white); font-size: 18px; margin-top: 14px; }
  .back__url {
    position: absolute;
    left: 0; right: 0;
    bottom: 50px;
    font-size: 17px;
    font-weight: 600;
  }
</style>
</head>
<body>
  <section class="card card--front" aria-label="Business card front">
    <div class="front__brand">
      <div class="brand-mark">
        <span class="brand-mark__dot"></span>
        <span class="brand-mark__name">Narvelo</span>
      </div>
      <p class="tagline">Talent • Leadership • Growth</p>
    </div>
    <div class="front__rule"></div>
    <div class="front__details">
      <p class="contact-name">Mara Quill</p>
      <p>President</p>
      <p>mara.quill@narvelo.com</p>
      <p class="contact-company">Narvelo Pty Ltd</p>
      <p>Fernbrook, California</p>
      <p>90418</p>
      <div class="contact-phones">
        <p><b>P:</b> 415.608.2210</p>
        <p><b>F:</b> 415.608.2211</p>
        <p><b>M:</b> 415.608.2212</p>
      </div>
    </div>
  </section>

  <section class="card card--back" aria-label="Business card back">
    <div class="back__brand">
      <div class="brand-mark">
        <span class="brand-mark__dot"></span>
        <span class="brand-mark__name">Narvelo</span>
      </div>
      <p class="tagline">Talent • Leadership • Growth</p>
    </div>
    <p class="back__url">www.narvelo.com</p>
  </section>
</body>
</html>
```